Marcus Pellow Carpentry & Joinery

Hello, I would like a flyer designed for my new business doing small projects in my local area for home-owners. I am a professional tradesman.
The type of work I am offering is:
- decks/decking
- external stairs & railings
- install windows & doors
- roofs & gutters
- small additions
- built-in wardrobes
- finish work
- demolition

It would be great if the flyer could mention these, or use phrasing that fits this kind of construction work.
My idea for a slogan was "new work and repairs to any age home".

Please also mention FREE QUOTES and have my email and phone number included on the flyer, along with my carpentry licence number, which I can provided.

I'd like a one page, single-sided flyer that could be printed as DL.
Colour and style is up to you! I'll be placing this flyer on counters & in the windows of local businesses, so something simple and eye-catching is preferred.

Thank you!

```html
<!DOCTYPE html>
<html lang="en">
<head>
<meta charset="utf-8">
<title>Marcus Pellow Carpentry &amp; Joinery – Flyer</title>
<link rel="stylesheet" href="https://fonts.googleapis.com/css2?family=Anton&family=Roboto+Condensed:wght@700&family=Open+Sans:wght@400;600&display=swap">
<style>
  :root {
    --sand: #f3ddb0;
    --frame-brown: #4e2f1e;
    --copy-brown: #5e4a38;
    --orange: #e66f0c;
    --blue: #2768bb;
    --ink: #1d1a17;
    --white: #ffffff;
    --tile-light: #c86a3c;
    --tile-dark: #8a3c1c;
    --wood: #d7b685;
  }
  * { box-sizing: border-box; margin: 0; padding: 0; }
  html, body { width: 1200px; height: 587px; overflow: hidden; }
  body { background: var(--sand); font-family: "Open Sans", sans-serif; }
  .flyer { position: relative; width: 1200px; height: 587px; background: var(--sand); overflow: hidden; }

  .wood-panel { position: absolute; left: 790px; top: 0; width: 410px; height: 587px;
    background: linear-gradient(90deg, #d9b98a, #cfa873 50%, #dcbd8f); }

  .intro-panel { position: absolute; left: 22px; top: 96px; width: 392px; height: 474px;
    border: 6px solid var(--frame-brown); border-top: none; background: var(--sand); }

  .roof-band { position: absolute; left: 0; top: 0; width: 1200px; height: 150px; }

  .headline { position: absolute; left: 0; top: 22px; width: 1200px; text-align: center;
    font-family: "Anton", sans-serif; font-size: 52px; font-weight: 400; color: var(--white);
    letter-spacing: 0.2px; line-height: 1.1; }

  .business-name { position: absolute; left: 48px; top: 172px; width: 350px; text-align: center;
    font-family: "Roboto Condensed", sans-serif; font-weight: 700; color: var(--blue);
    font-size: 40px; line-height: 1.05; text-transform: uppercase; }
  .business-name .name-line { display: block; }
  .business-name .trade-line { display: block; font-size: 27px; }

  .services { position: absolute; left: 82px; top: 298px; }
  .services-title { font-size: 20px; font-weight: 600; color: var(--orange); margin-bottom: 2px; }
  .services-list { list-style: none; }
  .services-list li { font-size: 21px; color: var(--ink); line-height: 28.3px; padding-left: 17px; position: relative; }
  .services-list li::before { content: ""; position: absolute; left: 2px; top: 11px; width: 8px; height: 8px;
    border-radius: 50%; background: var(--orange); }

  .pitch { position: absolute; left: 428px; top: 140px; width: 360px;
    font-family: "Roboto Condensed", sans-serif; font-weight: 700; font-size: 17.6px; line-height: 1.3;
    color: var(--copy-brown); }
  .pitch .firm { color: var(--blue); text-transform: uppercase; }

  .quote-call { position: absolute; left: 433px; top: 364px; width: 331px; text-align: center;
    font-family: "Roboto Condensed", sans-serif; font-weight: 700; font-size: 22px; color: var(--ink); }
  .phone-box { position: absolute; left: 433px; top: 398px; width: 331px; height: 53px; background: var(--orange);
    display: flex; align-items: center; justify-content: center; gap: 10px; }
  .phone-icon { width: 36px; height: 36px; }
  .phone-number { font-family: "Roboto Condensed", sans-serif; font-weight: 700; font-size: 39px; color: var(--ink); }
  .email-lead { position: absolute; left: 433px; top: 460px; width: 331px; text-align: center; font-size: 19px; color: var(--ink); }
  .email { position: absolute; left: 433px; top: 484px; width: 331px; text-align: center;
    font-size: 20px; font-weight: 600; color: var(--blue); }

  .gallery { position: absolute; left: 800px; top: 140px; display: grid;
    grid-template-columns: 186px 188px; grid-template-rows: 139px 139px 145px; gap: 5px 6px; }
  .photo { display: block; }
  .photo-deck { background: linear-gradient(160deg, #6f8a4a, #a5743f); }
  .photo-stairs { background: linear-gradient(160deg, #3f6a2e, #c7a27a); }
  .photo-windows { background: linear-gradient(160deg, #e9eee8, #b9b8a4); }
  .photo-roof { background: linear-gradient(160deg, #b8886a, #6c4a36); }
  .photo-wardrobe { background: linear-gradient(160deg, #caa57a, #6e4a2c); }
  .photo-demolition { background: linear-gradient(160deg, #7fa6d6, #8c7a5a); }
</style>
</head>
<body>
<main class="flyer">
  <div class="wood-panel" role="img" aria-label="Light timber plank background"></div>

  <section class="intro-panel"></section>

  <svg class="roof-band" viewBox="0 0 1200 150" role="img" aria-label="Terracotta roof tiles along the top edge">
    <defs>
      <linearGradient id="tileTone" x1="0" y1="0" x2="0" y2="1">
        <stop offset="0" stop-color="#a24a22"/>
        <stop offset="0.6" stop-color="#c8703f"/>
        <stop offset="1" stop-color="#8a3c1c"/>
      </linearGradient>
    </defs>
    <path d="M0 0 H1200 V110 Q1000 150 790 118 Q600 92 420 100 Q200 110 0 138 Z" fill="url(#tileTone)"/>
  </svg>

  <h1 class="headline">New construction or repair to houses of any age</h1>

  <h2 class="business-name">
    <span class="name-line">Marcus Pellow</span>
    <span class="trade-line">Carpentry &amp; Joinery</span>
  </h2>

  <div class="services">
    <p class="services-title">Our services include:</p>
    <ul class="services-list">
      <li>Deck building</li>
      <li>External stairs &amp; railings</li>
      <li>Windows/doors installation</li>
      <li>Roofs &amp; gutters</li>
      <li>Small additions</li>
      <li>Built-in wardrobes</li>
      <li>Finishing works</li>
      <li>Demolition</li>
    </ul>
  </div>

  <p class="pitch">If you are looking for a highly experienced carpentry and joinery service in the (state your area) and surrounding area, <span class="firm">Marcus Pellow Carpentry &amp; Joinery</span> offers a professional domestic joinery service, with outstanding craftsmanship and exceptional customer service.</p>

  <p class="quote-call">Call Now For a Free Quotation</p>
  <div class="phone-box">
    <svg class="phone-icon" viewBox="0 0 36 36" aria-hidden="true">
      <circle cx="18" cy="18" r="16" fill="none" stroke="#1d1a17" stroke-width="2.5"/>
      <path d="M13 9 q-3 2 -2 7 q2 7 8 11 q4 2 6 -1 l-3 -3 q-2 1 -3 0 q-3 -3 -4 -6 q0 -1 1 -2 z" fill="#1d1a17"/>
    </svg>
    <span class="phone-number">555.218.4406</span>
  </div>
  <p class="email-lead">or email at</p>
  <p class="email">marcuspellow@mailbox.com</p>

  <div class="gallery">
    <div class="photo photo-deck" role="img" aria-label="Timber deck built around a garden tree"></div>
    <div class="photo photo-stairs" role="img" aria-label="External timber stairs with black railings"></div>
    <div class="photo photo-windows" role="img" aria-label="Bright room with new arched windows and doors"></div>
    <div class="photo photo-roof" role="img" aria-label="Roof framing and shingles being installed"></div>
    <div class="photo photo-wardrobe" role="img" aria-label="Built-in timber wardrobe with lit shelving"></div>
    <div class="photo photo-demolition" role="img" aria-label="Excavator demolishing an old house"></div>
  </div>
</main>
</body>
</html>
```